CBD Boutique Business Card Needed

We are in need of a business card to reflect the direction of our latest products. We are a fully organic company in which our store and products are very heavy in wood and "natural" components. We decided to bring color into one of our brands and immediately knew this is where we needed to go.

We are NOT a cash grab CBD company. We could have done this wrong, slapped a label on a shit product and left it like that. I am passionate about sharing my experience with other veterans and opening a store and making it a comfortable place for others to come and see if they can have the same experience.

Target Market(s)

We are a dual market company. We do have a beauty line that will cover the costs of the majority of our business. But we also heavily cater to veterans and first responders. I am a veteran and this is how I found out about CBD. So the marketing needs to bring in our higher end beauty clientele but also be able to not put off our customers that readily need this.

Contact Information for Business Card

What we are looking for is a light, professional, boutique design that is is neither quite feminine or masculine. Attached is a picture of a store in Portland that we asked our store designer to get her inspiration from. But all natural wood and black outlines are what is mostly in there.

Attached are the following files:

Logo: An AI file with how we have our logo. I do not understand AI and have no idea why the letters are individual. The font is Adam. OLU is the logo and Tonics of Dawn is our tagline.

DC Portrait (front and back) cards I did originally found at a trade show that I absolutely loved...while it is mostly there and I would still be happy with them but it is me pretending to be you. I understand I am not and there is probably a lot wrong that all of you would see instantly and this is why I am here.

Dropper Bottle: This is our final product mock up

Water Color: I am semi flexible here. This water color is slightly different on every level of our brand. The color itself can change...we are not stuck on THIS particular one. If you happen to make a new one that is similar in style and we use it...then I will happily commission you to change the rest on our next product run. I am pretty sure you can use this statement as evidence later . =) .

But seriously, we heavily believe in pay it forward and will work with anyone here that may have a vision bigger than ours. The winner of this contest will get preferential consideration on our marketing materials (need letterhead etc. next, as well as a brochure, and website) so three more projects coming down the pipeline.

Information to use for your mockup is contained on the card images I have included. I would prefer CBD for wellness CBD for life to be more prominent. No where else on the card do we have CBD mentioned.

Font styles to use
Sans Serif

Colors

Designer to choose colors to be used in the design.

Requirements
Must have
• Double Sided
• Front: OLU logo on front of card will be raised embossed. Background is watercolor. One has been provided. Others are up for consideration. If the rest of your design is incredible and I don't like your watercolor I will just ask to swap it.
• Back: Standard information. Not stuck on anything here. I LOVE clean minimal designs. The bleed on the card I provided is a luxury...
• Font for title and OLU is Adam. Everything else I prefer san serif or as clean as possible.
Nice to have
• I Need to incorporate Naturally Nurturing somewhere on the card. Bold but not intrusive.

```html
<!DOCTYPE html>
<html lang="en">
<head>
<meta charset="utf-8">
<title>OLU – Business Card</title>
<link href="https://fonts.googleapis.com/css2?family=Raleway:wght@300;700&family=Roboto:wght@400;500&display=swap" rel="stylesheet">
<style>
  :root{
    --stage:#c9c9c9;
    --ink:#111111;
    --paper:#ffffff;
    --teal:#5bb8bb;
    --text:#222222;
  }
  html,body{margin:0;padding:0;overflow:hidden;}
  body{width:1200px;height:930px;background:var(--stage);position:relative;font-family:"Roboto",sans-serif;}
  .card{position:absolute;width:540px;height:310px;box-shadow:0 6px 18px rgba(0,0,0,.25);}
  .card--front{left:90px;top:120px;background:var(--ink);color:var(--paper);}
  .card--back{left:570px;top:490px;background:var(--paper);color:var(--ink);}
  .brand{position:absolute;font-family:"Raleway",sans-serif;font-weight:300;}
  .brand__name{display:block;font-size:92px;line-height:1;letter-spacing:6px;}
  .brand__tagline{display:block;font-size:20px;letter-spacing:2px;text-transform:uppercase;margin-top:6px;}
  .card--front .brand{left:170px;top:70px;}
  .slogan{position:absolute;left:0;right:0;bottom:42px;text-align:center;font-family:"Raleway",sans-serif;font-weight:700;font-size:13px;letter-spacing:.5px;}
  .slogan span{margin:0 5px;}
  .card--back .brand{left:40px;top:90px;}
  .contact{position:absolute;left:330px;top:92px;font-size:13px;line-height:1.35;color:var(--text);}
  .contact__name{font-size:20px;font-weight:500;color:var(--teal);margin:0;}
  .contact__role{font-size:11px;letter-spacing:1px;margin:0 0 12px;}
  .contact__address{margin:0 0 8px;}
  .contact__list{list-style:none;margin:0;padding:0 0 0 20px;}
  .contact__list li{display:flex;align-items:center;gap:6px;}
  .contact__list svg{width:10px;height:10px;flex:none;}
</style>
</head>
<body>
  <section class="card card--front" aria-label="Card front">
    <div class="brand">
      <span class="brand__name">OLU</span>
      <span class="brand__tagline">Tonics of Dawn</span>
    </div>
    <p class="slogan"><span>CBD FOR WELLNESS</span><span>CBD FOR LIFE</span></p>
  </section>

  <section class="card card--back" aria-label="Card back">
    <div class="brand">
      <span class="brand__name">OLU</span>
      <span class="brand__tagline">Tonics of Dawn</span>
    </div>
    <div class="contact">
      <p class="contact__name">Dana Whitfield</p>
      <p class="contact__role">OWNER / CEO</p>
      <p class="contact__address">4120 N Juniper Ave<br>Millbrook, AZ 85999<br>Suite 100</p>
      <ul class="contact__list">
        <li><svg viewBox="0 0 10 10"><path d="M2 1 L4 1 L4.5 3 L3.3 4 Q4.5 6 6 6.7 L7 5.5 L9 6 L9 8 Q5 9 2 5 Q1 3 2 1Z" fill="var(--teal)"/></svg>555.014.2287</li>
        <li><svg viewBox="0 0 10 10"><rect x="0.5" y="2" width="9" height="6" fill="none" stroke="var(--teal)"/><path d="M0.5 2 L5 5.5 L9.5 2" fill="none" stroke="var(--teal)"/></svg>hello@olu.life</li>
        <li><svg viewBox="0 0 10 10"><circle cx="5" cy="5" r="4.3" fill="none" stroke="var(--teal)"/><ellipse cx="5" cy="5" rx="1.8" ry="4.3" fill="none" stroke="var(--teal)"/><path d="M0.7 5 H9.3" stroke="var(--teal)"/></svg>www.olu.life</li>
      </ul>
    </div>
  </section>
</body>
</html>
```